Business Card front and back

I am looking for business card design. I really really like the design file I uploaded named 627788_19250069_3478263_85f427ee_image

Target Market(s)

Corporate Fitness High end Private country club

Industry/Entity Type

Fitness Industry

Contact Information for Business Card

The last image I like as an example I uploaded a bunch of my logos. The file labeled "the signature" is my business card information for you to use

Colors
0054AA
0677BA
7BADD7
CADEEF
E8F1F8

Requirements
Must have
• E-mail sigThe file I uploaded labeled "627788_19250069_3478263_85f427ee_image" with all the plus signs on the back if those could be the logo symbol I uploaded labeled "1 back.png"

```html
<!DOCTYPE html>
<html lang="en">
<head>
<meta charset="utf-8">
<title>Stridewell Athletics – Business Card Front and Back</title>
<link rel="stylesheet" href="https://fonts.googleapis.com/css2?family=Exo+2:wght@700&family=Source+Sans+3:wght@400&display=swap">
<style>
  :root {
    --stage: #e8e8e8;
    --card: #000000;
    --card-glow: #2a2a2a;
    --brand-blue: #4a7fc4;
    --ink-white: #ffffff;
    --motif-light: #5a5a5a;
    --motif-dark: #151515;
  }
  * { margin: 0; padding: 0; box-sizing: border-box; }
  html, body {
    width: 1200px; height: 960px; overflow: hidden;
    background: var(--stage);
  }
  .stage { position: relative; width: 1200px; height: 960px; }

  .card {
    position: absolute;
    width: 723px; height: 414px;
    background: var(--card);
    overflow: hidden;
  }
  .card--front { left: 208px; top: 59px; }
  .card--back { left: 302px; top: 496px;
    background: radial-gradient(ellipse 360px 260px at 300px 210px, var(--card-glow) 0%, var(--card) 70%);
  }

  /* front */
  .front-motif {
    position: absolute; inset: 0;
    background:
      radial-gradient(ellipse 220px 200px at 400px 200px, #1e1e1e 0%, rgba(0,0,0,0) 100%),
      linear-gradient(90deg, var(--card) 0%, var(--motif-dark) 40%, #262626 100%);
  }
  .wordmark {
    position: absolute; left: 0; right: 0; top: 246px;
    display: flex; justify-content: center; align-items: center; gap: 14px;
  }
  .wordmark__square {
    width: 26px; height: 26px; background: var(--brand-blue);
  }
  .wordmark__name {
    font-family: "Exo 2", sans-serif; font-weight: 700;
    font-size: 34px; line-height: 1; letter-spacing: 1px;
    color: var(--ink-white);
    text-transform: uppercase;
  }

  /* back */
  .holder {
    position: absolute; left: 44px; top: 52px;
    font-family: "Source Sans 3", sans-serif;
  }
  .holder__name {
    font-size: 39px; line-height: 1; color: var(--brand-blue);
    letter-spacing: -1px; text-transform: uppercase;
  }
  .holder__role { font-size: 18px; line-height: 1.1; color: var(--ink-white); margin-top: 2px; }

  .contacts {
    position: absolute; left: 44px; top: 267px;
    list-style: none;
    font-family: "Source Sans 3", sans-serif;
    font-size: 19px; color: var(--ink-white);
  }
  .contacts li { display: flex; align-items: center; height: 30px; }
  .contacts svg { width: 18px; height: 18px; margin-right: 11px; fill: var(--brand-blue); flex: none; }

  .back-motif {
    position: absolute; left: 354px; top: 116px; width: 344px; height: 256px;
    border-radius: 4px 60px 60px 4px;
    background: radial-gradient(ellipse 160px 130px at 300px 140px, var(--motif-light) 0%, #2c2c2c 55%, #111 100%);
  }
</style>
</head>
<body>
<main class="stage">

  <section class="card card--front" aria-label="Card front">
    <div class="front-motif" role="img" aria-label="Faint repeating brand symbol pattern fading in from the right"></div>
    <div class="wordmark">
      <span class="wordmark__square"></span>
      <span class="wordmark__name">Stridewell Athletics</span>
    </div>
  </section>

  <section class="card card--back" aria-label="Card back">
    <div class="holder">
      <p class="holder__name">Dale Varnow</p>
      <p class="holder__role">consultant</p>
    </div>

    <ul class="contacts">
      <li>
        <svg viewBox="0 0 20 20" aria-hidden="true"><path d="M2 8 L10 2 L18 8 V18 H2 Z M4 9 L10 13 L16 9 L10 5 Z"/></svg>
        dale@stridewellathletics.com
      </li>
      <li>
        <svg viewBox="0 0 20 20" aria-hidden="true"><path fill="none" stroke="#4a7fc4" stroke-width="1.6" d="M10 2a8 8 0 1 0 0.01 0M2 10h16M10 2c-4 4-4 12 0 16M10 2c4 4 4 12 0 16M4 5.5h12M4 14.5h12"/></svg>
        www.stridewellathletics.com
      </li>
      <li>
        <svg viewBox="0 0 20 20" aria-hidden="true"><path d="M4 2 L8 2 L9 6 L7 8 C8 11 9 12 12 13 L14 11 L18 12 L18 16 C18 17 17 18 16 18 C9 18 2 11 2 4 C2 3 3 2 4 2Z"/></svg>
        701-555-0148
      </li>
      <li>
        <svg viewBox="0 0 20 20" aria-hidden="true"><path d="M10 1 C6 1 4 4 4 7 C4 11 10 19 10 19 C10 19 16 11 16 7 C16 4 14 1 10 1 Z M10 5 A2.2 2.2 0 1 0 10.01 5 Z"/></svg>
        Upper Plains Region
      </li>
    </ul>

    <div class="back-motif" role="img" aria-label="Large brand symbol in graphite gradient"></div>
  </section>

</main>
</body>
</html>
```